Business Card Design

We are a manufacturing and distribution company with most of our customer base being supermarkets. We have established brand guidelines that are attached.

```html
<!DOCTYPE html>
<html lang="en">
<head>
<meta charset="utf-8">
<title>Velmora Business Card</title>
<link rel="stylesheet" href="https://fonts.googleapis.com/css2?family=Archivo:wght@400;500;700;800&display=swap">
<style>
  :root {
    --backdrop: #e3e4e6;
    --brand-red: #e01f2c;
    --brand-blue: #0a67ab;
    --ink: #1c1c1e;
    --paper: #ffffff;
    --card-shadow: rgba(0, 0, 0, 0.35);
  }
  * { margin: 0; padding: 0; box-sizing: border-box; }
  html, body {
    width: 1200px;
    height: 900px;
    overflow: hidden;
    background: var(--backdrop);
    font-family: "Archivo", "Helvetica Neue", Arial, sans-serif;
  }
  .card {
    position: absolute;
    top: 217px;
    width: 309px;
    height: 500px;
    box-shadow: 2px 3px 3px var(--card-shadow);
    overflow: hidden;
  }
  .card-front {
    left: 279px;
    border-radius: 0 60px 0 60px;
    background: linear-gradient(200deg, #0a67ab 0%, #3f4f86 28%, #8a3f66 55%, #d63444 82%, #e01f2c 100%);
  }
  .front-pattern {
    position: absolute;
    inset: 0;
    background: linear-gradient(180deg, rgba(255,255,255,0.06) 0%, rgba(255,255,255,0.12) 50%, rgba(255,255,255,0.04) 100%);
  }
  .front-wordmark {
    position: absolute;
    left: 0;
    right: 0;
    top: 424px;
    text-align: center;
    color: var(--paper);
    font-weight: 800;
    font-size: 40px;
    line-height: 48px;
    letter-spacing: 1px;
  }
  .card-back {
    left: 617px;
    border-radius: 60px 0 60px 0;
    background: var(--paper);
  }
  .back-wordmark {
    position: absolute;
    left: 0;
    right: 0;
    top: 144px;
    text-align: center;
    color: var(--ink);
    font-weight: 800;
    font-size: 42px;
    line-height: 52px;
    letter-spacing: 1px;
  }
  .contact-block {
    position: absolute;
    left: 32px;
    top: 308px;
    color: var(--ink);
  }
  .person-name {
    font-weight: 500;
    font-size: 21px;
    line-height: 1;
    letter-spacing: 0.2px;
  }
  .person-name .first { color: var(--brand-red); }
  .person-name .last { color: var(--brand-blue); }
  .person-title {
    font-size: 15px;
    line-height: 1;
    margin-top: 3px;
    letter-spacing: 0.3px;
  }
  .contact-list {
    list-style: none;
    margin-top: 16px;
    font-size: 14.5px;
  }
  .contact-list li {
    display: flex;
    align-items: center;
    gap: 5px;
    height: 18px;
  }
  .contact-icon { width: 13px; height: 13px; flex: none; }
  .address {
    margin-top: 13px;
    font-size: 14.5px;
    line-height: 18px;
  }
</style>
</head>
<body>
  <section class="card card-front">
    <div class="front-pattern" role="img" aria-label="Faint layered chevron pattern over the red-to-blue gradient"></div>
    <div class="front-wordmark">VELMORA</div>
  </section>

  <section class="card card-back">
    <div class="back-wordmark">VELMORA</div>
    <div class="contact-block">
      <p class="person-name"><span class="first">MARCUS</span> <span class="last">HALE</span></p>
      <p class="person-title">MANAGING DIRECTOR</p>
      <ul class="contact-list">
        <li>
          <svg class="contact-icon" viewBox="0 0 24 24" aria-hidden="true"><path fill="#e01f2c" d="M6.6 10.8a15.1 15.1 0 0 0 6.6 6.6l2.2-2.2a1 1 0 0 1 1-.25 11.4 11.4 0 0 0 3.6.57 1 1 0 0 1 1 1V20a1 1 0 0 1-1 1A17 17 0 0 1 3 4a1 1 0 0 1 1-1h3.5a1 1 0 0 1 1 1c0 1.25.2 2.45.57 3.57a1 1 0 0 1-.25 1z"/></svg>
          052-870 314 265
        </li>
        <li>
          <svg class="contact-icon" viewBox="0 0 24 24" aria-hidden="true"><rect x="2" y="5" width="20" height="14" fill="#e01f2c"/><path d="M2 5l10 8 10-8" fill="none" stroke="#fff" stroke-width="1.6"/></svg>
          hello@velmora.com
        </li>
        <li>
          <svg class="contact-icon" viewBox="0 0 24 24" aria-hidden="true"><g fill="none" stroke="#e01f2c" stroke-width="2"><circle cx="12" cy="12" r="9.5"/><ellipse cx="12" cy="12" rx="4.2" ry="9.5"/><path d="M2.5 12h19M4 7h16M4 17h16"/></g></svg>
          www.velmora-foods.com
        </li>
      </ul>
      <p class="address">88, Harbor Point Road<br>30217, Eastvale</p>
    </div>
  </section>
</body>
</html>
```